Business Card Design

We are a commercial real estate brokerage in San Francisco, leasing office buildings downtown.
I would like a clean, elegant look. Simple but powerful .

Industry/Entity Type

Business

Contact Information for Business Card

Colin Farrow
lic# 07281549
415.555.0172
colin@tarvo-commercial.example
tarvo-commercial.example

```html
<!DOCTYPE html>
<html lang="en">
<head>
<meta charset="utf-8">
<title>Tarvo Commercial – Business Card</title>
<link rel="stylesheet" href="https://fonts.googleapis.com/css2?family=Questrial&family=Source+Sans+3:wght@400;600&display=swap">
<style>
  :root {
    --stage: #000000;
    --card: #ffffff;
    --brand-blue: #7185a5;
    --ink: #222222;
    --muted: #6b6b6b;
    --skyline-light: #f1f1f1;
    --skyline-mid: #e6e6e6;
    --mark-grey: #8a8a8a;
  }
  * { margin: 0; padding: 0; box-sizing: border-box; }
  html, body {
    width: 1200px; height: 900px; overflow: hidden;
    background: var(--stage);
  }
  .canvas { position: relative; width: 1200px; height: 900px; }

  .card {
    position: absolute;
    width: 477px; height: 293px;
    background: var(--card);
    overflow: hidden;
  }
  .card--front { left: 116px; top: 275px; border-radius: 0 48px 0 48px; }
  .card--back  { left: 622px; top: 276px; height: 292px; border-radius: 48px 0 48px 0; }

  .skyline {
    position: absolute;
    background: linear-gradient(180deg, var(--skyline-light) 0%, var(--skyline-mid) 100%);
  }
  .card--front .skyline { left: 279px; top: 63px; width: 198px; height: 230px; opacity: .8; }
  .card--back .skyline  { left: 213px; top: 59px; width: 264px; height: 233px; }

  .brand { font-family: "Questrial", sans-serif; color: var(--brand-blue); position: absolute; line-height: 1; }
  .brand__name { display: block; }

  .card--front .brand-square {
    position: absolute; left: 40px; top: 43px; width: 56px; height: 56px;
    background: var(--mark-grey);
  }
  .card--front .divider {
    position: absolute; left: 136px; top: 32px; width: 2px; height: 76px;
    background: var(--muted);
  }
  .card--front .brand { left: 146px; top: 42px; }
  .card--front .brand__name--main { font-size: 44px; letter-spacing: 1px; }
  .card--front .brand__name--sub { font-size: 19px; letter-spacing: 1px; margin-top: 2px; }

  .card--back .brand { left: 43px; top: 178px; }
  .card--back .brand__name--main { font-size: 56px; letter-spacing: 1px; }
  .card--back .brand__name--sub { font-size: 24px; letter-spacing: 1px; margin-top: 2px; }

  .contact { position: absolute; left: 146px; top: 126px; font-family: "Source Sans 3", sans-serif; }
  .contact__name { font-size: 18px; font-weight: 600; color: var(--brand-blue); }
  .contact__licence { margin-top: 14px; font-size: 13px; color: var(--ink); font-weight: 600; }
  .contact__licence span { color: var(--brand-blue); font-weight: 400; }
  .contact__list { list-style: none; margin-top: 14px; }
  .contact__item {
    display: flex; align-items: center; gap: 6px;
    font-size: 13.5px; color: var(--ink); height: 20px;
  }
  .contact__icon { width: 11px; height: 11px; fill: var(--muted); flex: none; }
</style>
</head>
<body>
<main class="canvas">

  <section class="card card--front" aria-label="Business card front">
    <div class="skyline" role="img" aria-label="Faint skyline of downtown office towers"></div>
    <div class="brand-square"></div>
    <div class="divider"></div>
    <div class="brand">
      <span class="brand__name brand__name--main">TARVO</span>
      <span class="brand__name brand__name--sub">COMMERCIAL</span>
    </div>
    <div class="contact">
      <p class="contact__name">Colin Farrow</p>
      <p class="contact__licence"><span>Lic#</span> 07281549</p>
      <ul class="contact__list">
        <li class="contact__item">
          <svg class="contact__icon" viewBox="0 0 24 24"><path d="M6.6 10.8a15.1 15.1 0 0 0 6.6 6.6l2.2-2.2a1 1 0 0 1 1-.25 11.4 11.4 0 0 0 3.6.57 1 1 0 0 1 1 1V20a1 1 0 0 1-1 1A17 17 0 0 1 3 4a1 1 0 0 1 1-1h3.5a1 1 0 0 1 1 1c0 1.25.2 2.45.57 3.57a1 1 0 0 1-.25 1z"/></svg>
          415.555.0172
        </li>
        <li class="contact__item">
          <svg class="contact__icon" viewBox="0 0 24 24"><path d="M2 5h20v14H2z M2 5l10 7 10-7" fill="var(--muted)"/><path d="M3 6l9 6.5L21 6" fill="none" stroke="#fff" stroke-width="1.6"/></svg>
          colin@tarvo-commercial.example
        </li>
        <li class="contact__item">
          <svg class="contact__icon" viewBox="0 0 24 24"><path d="M10 14a4 4 0 0 0 5.7 0l4-4a4 4 0 0 0-5.7-5.7l-1.2 1.2M14 10a4 4 0 0 0-5.7 0l-4 4a4 4 0 0 0 5.7 5.7l1.2-1.2" fill="none" stroke="var(--muted)" stroke-width="2.4" stroke-linecap="round"/></svg>
          tarvo-commercial.example
        </li>
      </ul>
    </div>
  </section>

  <section class="card card--back" aria-label="Business card back">
    <div class="skyline" role="img" aria-label="Embossed skyline of downtown office towers above an arcade"></div>
    <div class="brand">
      <span class="brand__name brand__name--main">TARVO</span>
      <span class="brand__name brand__name--sub">COMMERCIAL</span>
    </div>
  </section>

</main>
</body>
</html>
```